Business card design for IT consulting company

Looking for a simple, modern, clean business card design.
Open to reworking our existing logo.

Attached is our current business cards which we do not like.
Ideally double sided with something simple on the back.
Rectangle / Horizonal only.
No rounded edges on the card.
White as the dominate color is preferred.

Target Market(s)

clients, legal, oil & gas, medical, professionals

Industry/Entity Type

IT, tech, consulting

Contact Information for Business Card

Name, Title, email, phone, cell, website

Font styles to use
Sans Serif

Requirements
Must have
• Clean design
Should not have
• loud colors or unusual fonts, etc

```html
<!DOCTYPE html>
<html lang="en">
<head>
<meta charset="utf-8">
<title>Kelvra Solutions – Business Card</title>
<link rel="stylesheet" href="https://fonts.googleapis.com/css2?family=Montserrat:wght@400;500;700&display=swap">
<style>
  :root {
    --backdrop: #d9dadb;
    --card-white: #ffffff;
    --card-black: #232323;
    --ink: #3a3a3a;
    --ink-soft: #4a4a4a;
    --accent: #ef6b7c;
  }
  * { box-sizing: border-box; margin: 0; padding: 0; }
  html, body {
    width: 1200px; height: 1200px; overflow: hidden;
    background: var(--backdrop);
    font-family: "Montserrat", sans-serif;
  }
  .sheet {
    width: 1200px; height: 1200px;
    display: flex; flex-direction: column; align-items: center; justify-content: center;
    gap: 50px;
  }
  .card {
    width: 700px; height: 400px; position: relative;
    box-shadow: 0 14px 30px rgba(0,0,0,0.18);
  }
  .card--front { background: var(--card-white); color: var(--ink); }
  .card--back { background: var(--card-black); display: flex; align-items: center; justify-content: center; }

  .brand { position: absolute; left: 48px; top: 44px; display: flex; align-items: center; gap: 14px; }
  .brand__square { width: 52px; height: 52px; background: var(--accent); }
  .brand__name { font-weight: 700; font-size: 34px; color: var(--ink); letter-spacing: -0.3px; }

  .divider { position: absolute; left: 0; top: 200px; width: 600px; height: 2px; background: var(--ink); }

  .person { position: absolute; right: 100px; text-align: right; }
  .person__name { top: 150px; font-size: 34px; font-weight: 500; letter-spacing: 1px; }
  .person__title { top: 212px; font-size: 13px; letter-spacing: 1.5px; color: var(--ink-soft); }

  .contacts { position: absolute; left: 48px; top: 250px; list-style: none; font-size: 15px; color: var(--ink-soft); }
  .contacts li { display: flex; align-items: center; gap: 12px; height: 24px; }
  .contacts svg { width: 13px; height: 13px; fill: none; stroke: var(--ink); stroke-width: 1.6; }

  .back-brand { display: flex; align-items: center; gap: 18px; }
  .back-brand__square { width: 70px; height: 70px; background: var(--accent); }
  .back-brand__name { font-weight: 700; font-size: 46px; color: #ffffff; }
</style>
</head>
<body>
<main class="sheet">
  <section class="card card--front" aria-label="Business card front">
    <div class="brand">
      <span class="brand__square"></span>
      <span class="brand__name">Kelvra Solutions</span>
    </div>
    <div class="divider"></div>
    <p class="person person__name">DANIEL MOREAU</p>
    <p class="person person__title">IT CONSULTANT</p>
    <ul class="contacts">
      <li><svg viewBox="0 0 16 16"><rect x="1.5" y="3.5" width="13" height="9"/><path d="M1.5 3.5 8 9l6.5-5.5"/></svg>daniel.moreau@kelvra.ca</li>
      <li><svg viewBox="0 0 16 16"><path d="M4 1.5l2.5 3-1.5 1.5c.8 2 2.5 3.7 4.5 4.5L11 9l3 2.5-1.5 2.5C7 14 2 9 1.5 3.5z"/></svg>(800) 555-0142</li>
      <li><svg viewBox="0 0 16 16"><rect x="4.5" y="1.5" width="7" height="13" rx="1"/><path d="M7 12.5h2"/></svg>(604) 555-0187</li>
      <li><svg viewBox="0 0 16 16"><circle cx="8" cy="8" r="6.5"/><ellipse cx="8" cy="8" rx="3" ry="6.5"/><path d="M1.5 8h13"/></svg>www.kelvra.ca</li>
    </ul>
  </section>

  <section class="card card--back" aria-label="Business card back">
    <div class="back-brand">
      <span class="back-brand__square"></span>
      <span class="back-brand__name">Kelvra</span>
    </div>
  </section>
</main>
</body>
</html>
```